kleines Übersetzungsbüro sucht Design für Folder
Zielgruppe
Als Selbständige betreibe ich ein Italienisch-Übersetzungsbüro, das mit qualitativ hochwertigen Übersetzungen und maßgeschneidertem Service wirbt. Meine Tätigkeiten drehen sich um die Fachbereiche Recht und PR/Marketing/Corporate Communication.
Aufgabenstellung
Die Broschüre soll dynamisch,frisch, luftig, aber professionell wirken und gerne an den Stil meiner Website angelehnt sein.
Eine leicht minimalistische Gestaltung mit farbigen Akzenten (z.B. grafische Elemente) ist durchaus willkommen, aber nicht zwingend. Wenn das Endergebnis stimmig und überzeugend ist, lasse ich mich gerne umstimmen.
Auf das genaue Format des Folders möchte ich mich nicht festlegen. Ob einfach gefalzt, mit Wickel- oder Z-Falz: die Wahl überlasse ich Ihnen.
Der Folder soll zunächst nur per Mail übermittelt bzw. online verfügbar sein. Es empfiehlt sich also ein Format, bei dem die Inhalte überschaubar dargestellt sind und auf einen Blick erfasst werden können.
Alle CI-Farben sollten bei der Gestaltung berücksichtigt werden.
Vorgaben für die Verwendung vom Bildmaterial siehe hochgeladenes Briefingdokument.
Die Broschüre soll die Botschaft vermitteln, dass es sich lohnt auf einen dynamischen, zuverlässigen Profi zu setzen, der für einen immer da ist und pfiffige Leistungen erbringt.

```html
<!DOCTYPE html>
<html lang="de">
<head>
<meta charset="utf-8">
<title>Folder – Übersetzungsbüro Italienisch</title>
<link href="https://fonts.googleapis.com/css2?family=Roboto:wght@400;500&display=swap" rel="stylesheet">
<style>
  :root {
    --cyan: #14b6ea;
    --lime: #bde300;
    --green-text: #8cc400;
    --ink: #1f1f1f;
    --rule: #d4d4d4;
    --paper: #ffffff;
  }
  * { margin: 0; padding: 0; box-sizing: border-box; }
  html, body { width: 1200px; height: 635px; overflow: hidden; background: var(--paper); }
  body { font-family: "Roboto", Arial, sans-serif; color: var(--ink); }
  .folder { position: relative; width: 1200px; height: 635px; background: var(--paper); }

  .desk-photo {
    position: absolute; left: 0; top: 0; width: 1200px; height: 262px;
    background:
      linear-gradient(to bottom, rgba(255,255,255,0) 55%, #fff 100%),
      linear-gradient(to right, #6fa32f 0%, #a8cf6a 9%, #eef0ec 18%, #f4f4f4 30%, #fafafa 48%, #e8e8e8 60%, #fbfbfb 72%, #e6e6e6 86%, #f2f2f2 100%);
  }

  .fold { position: absolute; top: 0; width: 1px; height: 635px; background: var(--rule); }
  .fold--1 { left: 302px; } .fold--2 { left: 601px; } .fold--3 { left: 901px; }

  .base-band { position: absolute; left: 0; bottom: 0; width: 1200px; height: 16px; background: var(--lime); }

  .panel { position: absolute; font-size: 9.3px; line-height: 13.9px; }
  .panel--portfolio { left: 24px; top: 322px; width: 256px; }
  .panel--services { left: 320px; top: 288px; width: 262px; }
  .panel--quality { left: 619px; top: 270px; width: 262px; }
  .panel--values { left: 919px; top: 270px; width: 262px; }

  .heading {
    color: var(--cyan); font-weight: 500; font-size: 12.6px; line-height: 17.4px;
    letter-spacing: 0.3px; text-transform: uppercase; margin-bottom: 2px;
  }
  .panel p + p, .panel p + ul, .panel ul + p { margin-top: 13.9px; }
  .panel ul { list-style: none; }
  .panel li { padding-left: 7.5px; text-indent: -7.5px; }
  .panel li::before { content: "-\00a0\00a0"; }
  .accent { color: var(--green-text); }
  .section-gap { margin-top: 18px; }

  .laptop-photo {
    position: absolute; left: 619px; top: 459px; width: 245px; height: 160px;
    background: linear-gradient(135deg, #f3f4f6 0%, #e6e8eb 45%, #cfd2d6 70%, #eef0f2 100%);
  }
</style>
</head>
<body>
<main class="folder">
  <div class="desk-photo" role="img" aria-label="Schreibtisch von oben: Grünpflanze, Spiralblock mit Stiften, Kaffeetasse und weiße Tastatur"></div>

  <div class="fold fold--1"></div>
  <div class="fold fold--2"></div>
  <div class="fold fold--3"></div>

  <section class="panel panel--portfolio">
    <h2 class="heading">Einige Highlights aus<br>meinem Portfolio</h2>
    <p>Speziell für juristische Texte wie: Verträge, AGB, Klagen, Urteile, Urkunden, gerichtliche Beschlüsse, Protokolle, Handelsregisterauszüge, Ausschreibungsunterlagen, Satzungen, Schriftsätze, usw.</p>
    <ul>
      <li>Übersetzungen</li>
      <li>Beglaubigungen</li>
      <li>Einholung von Apostillen</li>
      <li>4-und 6-Augenkontrolle</li>
      <li>Express-Service</li>
    </ul>
    <p>Speziell für PR- und Marketing- und imagesensible Texte wie: Pressemitteilungen, Websites, Newsletters, Mitarbeiter- und Kundenmagazine, Unternehmensberichte, Themenzeitungen, alle Texte für Kampagnen, Markt- und Organisationskommunikation, Corporate Reputation und Social Networks, usw.</p>
  </section>

  <section class="panel panel--services">
    <ul>
      <li>Übersetzung, Adaptation und Transkreation in Informations- oder Publikationsqualität</li>
      <li>Briefing im Vorfeld der Projektumsetzung</li>
      <li>Erstellung kundenspezifischer Translation Memories</li>
      <li>4-und 6-Augenkontrolle</li>
      <li>Gut-zum-Druck</li>
    </ul>
    <h2 class="heading section-gap">Ihr direkter Draht zum<br>Übersetzungsprofi</h2>
    <p>Wenn Sie eine Übersetzungsagentur beauftragen, haben Sie zwar einen direkten Ansprechpartner. Dieser ist jedoch nicht für Ihre Übersetzung zuständig, sondern bearbeitet lediglich den Auftrag und gibt ihn an einen Übersetzer weiter. Wer diese Übersetzung letztendlich macht, erfahren Sie meistens nicht, auch nicht, wie qualifiziert Ihr Übersetzer tatsächlich ist. Bei mir hingegen wissen Sie, mit wem Sie es zu tun haben. Ich bin <span class="accent">Ihre unmittelbare Ansprechpartnerin,</span> kann gezielt auf Ihre individuellen Wünsche und Bedürfnisse eingehen und in jeder Phase des Auftrags mit Ihnen gemeinschaftlich am Gelingen Ihres Projektes arbeiten. Auf dem kleinen Dienstweg ist die Zusammenarbeit nicht nur <span class="accent">persönlicher,</span> sondern auch effizienter und <span class="accent">passgenauer</span> – genau das, was Sie benötigen!</p>
  </section>

  <section class="panel panel--quality">
    <h2 class="heading">Ihre Investition in Qualität</h2>
    <p>Aufgrund ihres hohen administrativen Aufwandes verlangen Übersetzungsagenturen ein nicht unerhebliches Honorar, der Übersetzer, der letzten Endes mit dem Auftrag betraut wird, erhält aber meistens nur einen minimalen Teil davon. Das heißt, auch wenn Sie selbst einen angemessenen Preis für Ihre Übersetzung zahlen, erledigt am anderen Ende jemand diese zu einem Dumping-Preis. Hier ist jedoch echte Qualität nicht zu erwarten. Investieren Sie daher lieber direkt in das Endprodukt eines Profis – ohne, dass ein zwischengeschalteter Vermittler weitere Kosten verursacht. Bei mir fließt jeder Cent garantiert in <span class="accent">Qualitätsarbeit!</span></p>
  </section>

  <div class="laptop-photo" role="img" aria-label="Hände tippen auf der Tastatur eines silbernen Laptops"></div>

  <section class="panel panel--values">
    <h2 class="heading">Meine Werte – Ihr Mehrwert</h2>
    <p>Meine Werte sind Ihr garantierter Mehrwert. Da Sie keine Umwege über ein Vermittlungsbüro gehen müssen, führt Ihr Auftrag Sie direkt zu mir. Ich stehe Ihnen als persönliche Ansprechpartnerin zur Verfügung – auch in Zeiten, in denen Übersetzungsbüros längst in den Feierabend oder ins Wochenende gegangen sind. <span class="accent">Auf kurzem Kommunikationsweg</span> erreichen Sie mich nahezu jederzeit per E-Mail oder telefonisch. Das ist Ihr Vorteil, gerade wenn es mal mit einer Übersetzung besonders eilig sein sollte. Bei aller <span class="accent">Unkompliziertheit</span> werden <span class="accent">Professionalität, Diskretion</span> und <span class="accent">Termineinhaltung</span> bei mir großgeschrieben. Dabei biete ich Ihnen <span class="accent">maximale Transparenz:</span> In der Projektabwicklung, der Preisgestaltung und schließlich der Honorarabrechnung behalten Sie jederzeit den Überblick. Dies gibt Ihnen die Planungssicherheit, die Sie brauchen.</p>
    <p>Setzen Sie daher auf:</p>
    <ul>
      <li>Professionalität</li>
      <li>Transparenz</li>
      <li>kurze Wege</li>
      <li>persönliche Beziehungen</li>
      <li>kompromisslose Qualität</li>
    </ul>
  </section>

  <div class="base-band"></div>
</main>
</body>
</html>
```